依頼詳細
PCとスマホデザインの両方納品をいただきますが、
まずはデザインイメージが確認しやすいPCページのみの提案をお願いします。
PCページはアートボード幅を1366px、コンテンツ幅を1000pxのもので作成してください。
スマホページは当選者に納品時にお願いしたいと思います。
スマホサイズは横幅750pxのサイズで作成してください。

レスポンシブウェブデザインを意識したデザインでお願いします。

デザインに関しては、添付してあるデザインレイアウト設計シートを基にお願いします。
参考サイトのURLはデザインレイアウト設計シートに記載してあります。
画像データについては、フリー素材から流用してイメージ画像に当て込んでください。

足りない場合は、一旦他のサイトの写真をサンプルとして入れてください。(サンプルなどの表記をお願いします)
また、購入が必要な写真などを利用した場合、価格とサイト名を教えてください。
ページ数
1ページ
希望イメージ
シンプル 複雑
単色 カラフル
暗い 明るい
日常 高級
遊び心 厳粛
未来的 伝統的
女性的 男性的
希望する色
緑系
納品ファイル
• イラストレーター形式 (.ai)
• フォトショップ形式 (.psd)
• PNG形式 (.png)
補足説明
上記のいずれか1つ(アウトラインありとなしの2つ)と高解像度JPGを納品お願いします。

```html
<!DOCTYPE html>
<html lang="ja">
<head>
<meta charset="utf-8">
<title>株式会社みどり環境</title>
<link href="https://fonts.googleapis.com/css2?family=Noto+Sans+JP:wght@400;500;700;900&display=swap" rel="stylesheet">
<style>
:root{
  --green:#2e9e63;
  --green-dark:#1f6b43;
  --green-pale:#eaf5ee;
  --green-mist:#f4f8f3;
  --forest:#24432f;
  --forest-deep:#1b3324;
  --orange:#f0a031;
  --orange-num:#e8772e;
  --line:#38b24a;
  --ink:#333;
  --muted:#777;
  --white:#fff;
}
*{box-sizing:border-box;margin:0;padding:0}
html,body{width:1200px;height:4912px;overflow:hidden}
body{font-family:"Noto Sans JP",sans-serif;color:var(--ink);background:var(--white);font-size:14px;line-height:1.6}
.wrap{width:880px;margin:0 auto;position:relative}
.photo{background:linear-gradient(135deg,#b9c9bd,#7f9a88);}

/* header */
.site-header{height:112px}
.site-header .wrap{display:flex;align-items:center;justify-content:space-between;height:112px}
.brand{display:flex;align-items:center;gap:10px}
.brand-lead{font-size:10px;color:var(--muted);line-height:1.3}
.brand-mark{width:34px;height:34px;border-radius:50%;background:var(--green)}
.brand-name{font-size:26px;font-weight:700;color:var(--green-dark)}
.header-contact{display:flex;align-items:center;gap:10px}
.header-tel{text-align:right;line-height:1.2}
.header-tel small{font-size:10px;color:var(--muted);display:block}
.header-tel strong{font-size:26px;color:var(--green-dark);font-weight:900;letter-spacing:.02em}
.hbtn{width:58px;height:44px;border-radius:4px;color:#fff;font-size:10px;font-weight:700;display:flex;align-items:center;justify-content:center;text-align:center;line-height:1.2}
.hbtn.line{background:var(--line)}.hbtn.mail{background:var(--orange)}
.global-nav{height:40px;background:var(--green-pale)}
.global-nav ul{list-style:none;display:flex;width:880px;margin:0 auto;height:40px}
.global-nav li{flex:1;text-align:center;line-height:40px;font-size:13px;font-weight:500;color:var(--green-dark);border-right:1px solid #cfe4d6}
.global-nav li.on{background:var(--green);color:#fff}

/* hero */
.hero{height:460px;background:linear-gradient(180deg,#f1f8f3,#fff);position:relative;overflow:hidden}
.hero-visual{position:absolute;right:0;top:0;width:760px;height:460px;clip-path:polygon(22% 0,100% 0,100% 100%,0 100%,10% 50%)}
.hero-copy{position:absolute;left:110px;top:70px;z-index:2}
.hero-copy h1{font-size:50px;font-weight:900;color:var(--green);line-height:1.25;text-shadow:0 0 8px #fff}
.hero-band{display:inline-block;margin-top:14px;background:var(--green);color:#fff;font-size:20px;font-weight:700;padding:6px 18px}
.hero-record{margin-top:22px;width:250px;text-align:center;color:var(--green-dark)}
.hero-record span{display:block;background:var(--green);color:#fff;font-size:14px;border-radius:20px;padding:2px 0;width:150px;margin:0 auto}
.hero-record strong{font-size:50px;font-weight:900;color:var(--green);line-height:1.2}
.hero-record strong small{font-size:22px}

/* promises */
.promises{height:520px;background:linear-gradient(180deg,#fff 0,#f4f7f3 40%,#e3e9e3 100%);padding-top:50px;position:relative}
.section-title{text-align:center}
.section-title p{font-size:14px;color:var(--ink)}
.section-title h2{font-size:30px;font-weight:700;color:var(--ink)}
.section-title h2 em{font-style:normal;color:var(--orange-num);font-size:40px}
.promise-list{list-style:none;display:grid;grid-template-columns:1fr 1fr;gap:30px 70px;margin-top:40px}
.promise-list li{border-bottom:1px dashed #b7c9bb;padding-bottom:10px}
.promise-list h3{font-size:19px;font-weight:700;color:var(--green-dark)}
.promise-list h3 b{color:var(--orange-num);font-size:22px;margin-right:10px;font-style:italic}
.promise-list p{font-size:11px;color:var(--muted);padding-left:40px}

/* cta */
.cta{height:210px;background:var(--green);color:#fff;text-align:center;position:relative}
.cta h2{padding-top:38px;font-size:26px;font-weight:700}
.cta h2 span{background:#fff;color:var(--green);padding:0 14px;border-radius:4px;margin-left:6px}
.cta p{margin-top:16px;font-size:15px;line-height:1.8}
.cta-figure{position:absolute;right:200px;top:14px;width:110px;height:180px;border-radius:50px 50px 20px 20px;background:linear-gradient(180deg,#8fcf6e,#4c9a45)}
.contact-row{height:120px;background:var(--green-mist)}
.contact-row .wrap{display:flex;align-items:center;height:120px;gap:26px}
.tel-block{flex:1;display:flex;align-items:center;gap:10px}
.tel-block strong{font-size:40px;font-weight:900;color:var(--green-dark);line-height:1}
.tel-block small{display:block;font-size:11px;color:var(--muted);margin-top:4px}
.cbtn{width:200px;height:58px;border-radius:6px;color:#fff;font-weight:700;font-size:15px;display:flex;align-items:center;justify-content:center;gap:8px}
.cbtn.line{background:var(--line)}.cbtn.mail{background:var(--orange)}
.ask-bar{height:48px;background:var(--green);color:#fff;text-align:center;line-height:48px;font-size:16px;font-weight:700;margin-top:8px}

/* services */
.services{height:800px;background:var(--green-mist);margin-top:12px;padding-top:90px}
.service-grid{list-style:none;display:grid;grid-template-columns:repeat(4,192px);gap:30px 36px;justify-content:center;margin-top:160px}
.service-grid li{height:180px;background:#fff;box-shadow:0 2px 6px rgba(0,0,0,.08)}
.service-grid .photo{height:136px}
.service-grid span{display:block;font-size:14px;font-weight:700;padding:10px 14px;border-left:4px solid var(--green);margin-top:6px}

/* works */
.works{height:950px;background:#fff;padding-top:80px}
.works-intro{display:flex;justify-content:space-between;margin-top:60px;align-items:center}
.works-text h3{font-size:22px;font-weight:700;color:var(--green-dark)}
.works-text h3 strong{color:var(--orange-num);font-size:30px}
.works-text p{font-size:13px;color:var(--ink);margin-top:12px;line-height:1.9}
.works-photo{width:200px;height:200px;border-radius:50%}
.works-cards{display:grid;grid-template-columns:repeat(3,1fr);gap:40px;margin-top:40px}
.works-cards div{height:300px;background:#fff;border-radius:10px;box-shadow:0 2px 10px rgba(0,0,0,.12)}
.more-btn{display:block;width:220px;height:44px;margin:40px auto 0;background:var(--green);color:#fff;border-radius:22px;text-align:center;line-height:44px;font-size:14px;font-weight:700}

/* banners */
.banners{height:380px;background:var(--green-mist);padding-top:40px}
.banners .wrap{display:grid;grid-template-columns:1fr 1fr;gap:30px}
.banner{height:300px;background:#fff;border-radius:10px;overflow:hidden;box-shadow:0 2px 8px rgba(0,0,0,.1)}
.banner .photo{height:240px}
.banner p{height:60px;line-height:60px;padding-left:30px;font-size:22px;font-weight:700;color:var(--green-dark)}

/* news */
.news{height:380px;padding-top:60px}
.news .wrap{display:flex;gap:40px}
.news-head{width:300px;background:var(--green-mist);padding:26px}
.news-head h2{font-size:26px;font-weight:700}
.news-head p{font-size:12px;color:var(--muted)}
.news-list{flex:1;list-style:none;border-top:1px solid #ddd}
.news-list li{display:flex;gap:30px;padding:12px 10px;border-bottom:1px solid #ddd;font-size:13px}
.news-list time{color:var(--muted)}

/* footer */
.site-footer{height:420px;background:var(--forest);color:#dfe9e2;padding-top:48px}
.footer-cols{display:flex;gap:40px}
.footer-info{width:330px;font-size:12px;line-height:1.8}
.footer-info .brand-name{color:#fff;font-size:24px}
.footer-info .tel{font-size:26px;font-weight:900;color:#fff}
.footer-nav{display:flex;gap:36px;font-size:13px}
.footer-nav ul{list-style:none}
.footer-nav li{margin-bottom:6px}
.footer-nav li::before{content:"▸ ";color:var(--green)}
.footer-nav li.sub{padding-left:14px;font-size:12px;color:#b9ccbf}
.footer-nav li.sub::before{content:"- "}
.social{display:flex;justify-content:center;gap:20px;margin-top:20px}
.social span{width:28px;height:28px;border-radius:50%;background:#dfe9e2}
.copyright{height:76px;background:var(--forest-deep);color:#9fb7a7;font-size:11px;text-align:center;line-height:76px}
</style>
</head>
<body>

<header class="site-header">
  <div class="wrap">
    <div class="brand">
      <span class="brand-mark"></span>
      <div>
        <p class="brand-lead">浄化槽点検保守・不用品回収・廃棄物処理ならお任せください</p>
        <p class="brand-name">株式会社みどり環境</p>
      </div>
    </div>
    <div class="header-contact">
      <div class="header-tel"><small>お見積り・ご相談はお気軽に</small><strong>0120-481-572</strong><small>平日8:30〜17:30（土日祝休）</small></div>
      <span class="hbtn line">LINE<br>見積り</span>
      <span class="hbtn mail">メール<br>問合せ</span>
    </div>
  </div>
</header>
<nav class="global-nav">
  <ul><li class="on">ホーム</li><li>サービス一覧</li><li>よくある質問</li><li>作業実績</li><li>会社案内</li></ul>
</nav>

<section class="hero">
  <div class="hero-visual photo" role="img" aria-label="作業スタッフや車両の写真を三角形に組み合わせたビジュアル"></div>
  <div class="hero-copy">
    <h1>信頼される<br>納得・安心サービス</h1>
    <p class="hero-band">浄化槽点検保守 / 不用品回収 / 廃棄物処理</p>
    <div class="hero-record"><span>年間実績</span><strong>23,449<small>件</small></strong></div>
  </div>
</section>

<section class="promises">
  <div class="wrap">
    <div class="section-title"><p>安心してご利用いただける</p><h2><em>6</em>つのお約束</h2></div>
    <ul class="promise-list">
      <li><h3><b>01</b>充実のサポート</h3><p>ご依頼からアフターまで担当が丁寧にサポートいたします。</p></li>
      <li><h3><b>04</b>信頼できるプロの技術</h3><p>経験豊富なスタッフが確かな技術で対応いたします。</p></li>
      <li><h3><b>02</b>自宅にいるだけでOK</h3><p>お立ち会いのみで搬出から片付けまでお任せください。</p></li>
      <li><h3><b>05</b>安心保証サービス</h3><p>万が一の場合も保証制度でしっかり対応いたします。</p></li>
      <li><h3><b>03</b>配慮を忘れません</h3><p>ご近所への配慮を第一に静かに作業いたします。</p></li>
      <li><h3><b>06</b>お急ぎの方も大歓迎</h3><p>ご連絡いただければ当日の対応も可能です。</p></li>
    </ul>
  </div>
</section>

<section class="cta">
  <h2>お見積り・ご相談<span>無料！</span></h2>
  <p>浄化槽のことや不用品回収・廃棄物の処理など<br>お客様のお困りごとに対して丁寧にご対応いたします。</p>
  <div class="cta-figure" role="img" aria-label="会社キャラクターのイラスト"></div>
</section>
<div class="contact-row">
  <div class="wrap">
    <div class="tel-block">
      <svg width="40" height="40" viewBox="0 0 24 24"><path fill="#1f6b43" d="M6.6 10.8a15 15 0 0 0 6.6 6.6l2.2-2.2c.3-.3.7-.4 1-.2 1.1.4 2.3.6 3.6.6.6 0 1 .4 1 1V20c0 .6-.4 1-1 1A17 17 0 0 1 3 4c0-.6.4-1 1-1h3.5c.6 0 1 .4 1 1 0 1.3.2 2.5.6 3.6.1.3 0 .7-.2 1z"/></svg>
      <div><strong>0120-481-572</strong><small>平日8:30〜17:30（土日祝休み）</small></div>
    </div>
    <span class="cbtn line">LINEで簡単見積</span>
    <span class="cbtn mail"><svg width="20" height="16" viewBox="0 0 20 16"><rect x="1" y="1" width="18" height="14" fill="none" stroke="#fff" stroke-width="2"/><path d="M1 1l9 8 9-8" fill="none" stroke="#fff" stroke-width="2"/></svg>メールでお問い合わせ</span>
  </div>
</div>
<div class="ask-bar">お気軽にお問い合わせください</div>

<section class="services">
  <div class="section-title"><h2>サービス紹介</h2></div>
  <ul class="service-grid">
    <li><div class="photo" role="img" aria-label="浄化槽点検の写真"></div><span>浄化槽維持管理</span></li>
    <li><div class="photo" role="img" aria-label="家財の片付け作業の写真"></div><span>丸ごとお片づけ</span></li>
    <li><div class="photo" role="img" aria-label="不用品回収の写真"></div><span>不用品回収</span></li>
    <li><div class="photo" role="img" aria-label="廃棄物処理の写真"></div><span>廃棄整理</span></li>
    <li><div class="photo" role="img" aria-label="遺品整理の写真"></div><span>遺品整理</span></li>
    <li><div class="photo" role="img" aria-label="住まいのサービスのイメージ"></div><span>住まいるみどり</span></li>
    <li><div class="photo" role="img" aria-label="その他サービスの写真"></div><span>その他サービス</span></li>
  </ul>
</section>

<section class="works">
  <div class="wrap">
    <div class="section-title"><h2>作業実績</h2></div>
    <div class="works-intro">
      <div class="works-text">
        <h3>年間作業実績 <strong>23,449</strong>件！</h3>
        <p>みどり環境では、年間23,449件の作業実績がございます。<br>不用品回収はもちろん、不用品処理・遺品整理・生前整理など、<br>お客様のあらゆるお困りごとを解決いたします。</p>
      </div>
      <div class="works-photo photo" role="img" aria-label="スタッフ集合写真"></div>
    </div>
    <div class="works-cards"><div></div><div></div><div></div></div>
    <span class="more-btn">作業実績一覧 ›</span>
  </div>
</section>

<section class="banners">
  <div class="wrap">
    <div class="banner"><div class="photo" role="img" aria-label="会社の看板の写真"></div><p>会社案内 ›</p></div>
    <div class="banner"><div class="photo" role="img" aria-label="スタッフが働く様子の写真"></div><p>採用ページ ›</p></div>
  </div>
</section>

<section class="news">
  <div class="wrap">
    <div class="news-head"><h2>新着情報</h2><p>みどり環境からのお知らせや最新情報をお届けします。</p></div>
    <ul class="news-list">
      <li><time>2019年6月1日</time>年末年始の営業についてのお知らせ</li>
      <li><time>2019年5月20日</time>ホームページをリニューアルしました</li>
      <li><time>2019年5月10日</time>採用情報を更新しました</li>
      <li><time>2019年4月28日</time>大型連休中の営業について</li>
    </ul>
  </div>
  <span class="more-btn">新着情報一覧 ›</span>
</section>

<section class="cta">
  <h2>お見積り・ご相談<span>無料！</span></h2>
  <p>浄化槽のことや不用品回収・廃棄物の処理など<br>お客様のお困りごとに対して丁寧にご対応いたします。</p>
  <div class="cta-figure" role="img" aria-label="会社キャラクターのイラスト"></div>
</section>
<div class="contact-row">
  <div class="wrap">
    <div class="tel-block">
      <svg width="40" height="40" viewBox="0 0 24 24"><path fill="#1f6b43" d="M6.6 10.8a15 15 0 0 0 6.6 6.6l2.2-2.2c.3-.3.7-.4 1-.2 1.1.4 2.3.6 3.6.6.6 0 1 .4 1 1V20c0 .6-.4 1-1 1A17 17 0 0 1 3 4c0-.6.4-1 1-1h3.5c.6 0 1 .4 1 1 0 1.3.2 2.5.6 3.6.1.3 0 .7-.2 1z"/></svg>
      <div><strong>0120-481-572</strong><small>平日8:30〜17:30（土日祝休み）</small></div>
    </div>
    <span class="cbtn line">LINEで簡単見積</span>
    <span class="cbtn mail"><svg width="20" height="16" viewBox="0 0 20 16"><rect x="1" y="1" width="18" height="14" fill="none" stroke="#fff" stroke-width="2"/><path d="M1 1l9 8 9-8" fill="none" stroke="#fff" stroke-width="2"/></svg>メールでお問い合わせ</span>
  </div>
</div>
<div class="ask-bar">お気軽にお問い合わせください</div>

<footer class="site-footer">
  <div class="wrap">
    <div class="footer-cols">
      <div class="footer-info">
        <p>浄化槽点検保守・不用品回収・廃棄物処理</p>
        <p class="brand-name">株式会社みどり環境</p>
        <p class="tel">0120-481-572</p>
        <p>〒000-0000 緑ヶ丘市若葉町1-2-3</p>
        <p>TEL 000-000-0000 / FAX 000-000-0001</p>
        <p>e-mail：info@midori-kankyo.example</p>
      </div>
      <div class="footer-nav">
        <ul><li>サービス一覧</li><li class="sub">浄化槽維持管理</li><li class="sub">丸ごとお片づけ</li><li class="sub">不用品回収</li><li class="sub">廃棄整理</li><li class="sub">遺品整理</li><li class="sub">住まいるみどり</li><li class="sub">その他サービス</li></ul>
        <ul><li>よくある質問</li><li>作業実績</li><li>会社案内</li><li>新着情報</li></ul>
        <ul><li>無料お見積り</li><li>お問い合わせ</li></ul>
      </div>
    </div>
    <div class="social"><span></span><span></span><span></span></div>
  </div>
</footer>
<div class="copyright">Copyright © 2019 株式会社みどり環境 All Rights Reserved.</div>

</body>
</html>
```